Business Cards for Internet Security Company

Awesome designers! This is the opportunity to help design cards for a forward thinking network security company. They use threat information gathered from peer groups to make intelligent decisions on what threats are relevant and which arent. ( not that you need this to do designs, but just so you know where they are coming from. ) :-)

We'd like to see a two side design and the deliverables will be in illustrator 4. The logo is attached and the logo colors are attached in the JPG and I've attached a an eps of the logo and icon

Security

```html
<!DOCTYPE html>
<html lang="en">
<head>
<meta charset="utf-8">
<title>Kelvara Business Cards</title>
<link href="https://fonts.googleapis.com/css2?family=Questrial&family=Open+Sans:wght@400&display=swap" rel="stylesheet">
<style>
  :root {
    --backdrop: #d6d6d6;
    --navy-blue: #2f6b8e;
    --bright-blue: #3b84bf;
    --ink-blue: #2b5f86;
    --paper: #ffffff;
    --text-grey: #4a4a4a;
  }
  * { margin: 0; padding: 0; box-sizing: border-box; }
  html, body { width: 1200px; height: 750px; overflow: hidden; }
  body {
    background: radial-gradient(ellipse at 45% 30%, #ececec 0%, var(--backdrop) 70%, #c4c4c4 100%);
    position: relative;
    font-family: "Questrial", sans-serif;
  }
  .card {
    position: absolute;
    top: 232px;
    width: 500px;
    height: 286px;
    border-radius: 18px;
    overflow: hidden;
    box-shadow: 0 6px 14px rgba(0,0,0,0.18);
  }
  .card-back { left: 70px; }
  .card-front { left: 630px; }
  .card-shapes { position: absolute; inset: 0; display: block; }

  .brand {
    position: absolute;
    display: flex;
    align-items: center;
    gap: 10px;
    font-family: "Questrial", sans-serif;
    font-weight: 400;
    letter-spacing: 0.5px;
  }
  .brand-dot {
    width: 30px; height: 30px;
    border-radius: 50%;
  }
  .card-back .brand { left: 42px; bottom: 38px; font-size: 44px; color: var(--paper); }
  .card-back .brand-dot { background: var(--paper); }
  .card-front .brand { left: 36px; top: 34px; font-size: 42px; color: var(--ink-blue); }
  .card-front .brand-dot { background: var(--ink-blue); }

  .holder-name {
    position: absolute;
    left: 78px; top: 118px;
    font-size: 25px;
    font-weight: 400;
    color: var(--ink-blue);
  }
  .name-rule {
    position: absolute;
    left: 74px; top: 154px;
    width: 200px; height: 1px;
    background: var(--bright-blue);
  }
  .contact-list {
    position: absolute;
    left: 80px; top: 164px;
    list-style: none;
    font-family: "Open Sans", sans-serif;
    font-size: 11px;
    color: var(--text-grey);
  }
  .contact-list li { display: flex; align-items: center; gap: 8px; height: 20px; }
  .contact-icon { width: 12px; height: 12px; flex: none; }
  .address {
    position: absolute;
    right: 22px; bottom: 20px;
    display: flex; align-items: center; gap: 6px;
    font-family: "Open Sans", sans-serif;
    font-size: 10px;
    color: var(--paper);
  }
  .address .contact-icon { width: 13px; height: 13px; }
</style>
</head>
<body>

  <section class="card card-back" aria-label="Card back">
    <svg class="card-shapes" viewBox="0 0 500 286" aria-hidden="true">
      <rect width="500" height="286" fill="var(--navy-blue)"/>
      <circle cx="370" cy="-30" r="215" fill="var(--bright-blue)"/>
      <circle cx="385" cy="-50" r="190" fill="var(--paper)"/>
    </svg>
    <div class="brand"><span class="brand-dot"></span>Kelvara</div>
  </section>

  <section class="card card-front" aria-label="Card front">
    <svg class="card-shapes" viewBox="0 0 500 286" aria-hidden="true">
      <rect width="500" height="286" fill="var(--paper)"/>
      <path d="M0,262 C150,292 250,235 320,150 S440,35 500,28 L500,286 L0,286 Z" fill="var(--bright-blue)"/>
      <path d="M0,286 C170,296 275,250 342,168 S455,62 500,56 L500,286 Z" fill="var(--navy-blue)"/>
    </svg>

    <div class="brand"><span class="brand-dot"></span>Kelvara</div>
    <h1 class="holder-name">Alex Morrow</h1>
    <div class="name-rule"></div>
    <ul class="contact-list">
      <li>
        <svg class="contact-icon" viewBox="0 0 12 12" aria-hidden="true">
          <circle cx="6" cy="6" r="6" fill="var(--ink-blue)"/>
          <path d="M4,3.2 L5,3 L5.6,4.6 L5,5.1 C5.3,5.9 6,6.6 6.9,7 L7.4,6.4 L9,7 L8.8,8 C6,8.3 3.7,6 4,3.2 Z" fill="var(--paper)"/>
        </svg>
        010-482-7365
      </li>
      <li>
        <svg class="contact-icon" viewBox="0 0 12 12" aria-hidden="true">
          <circle cx="6" cy="6" r="6" fill="var(--ink-blue)"/>
          <circle cx="6" cy="6" r="3.2" fill="none" stroke="var(--paper)" stroke-width="0.8"/>
          <path d="M2.8,6 H9.2 M6,2.8 V9.2" stroke="var(--paper)" stroke-width="0.8"/>
        </svg>
        www.alexmorrow.net
      </li>
    </ul>
    <p class="address">
      <svg class="contact-icon" viewBox="0 0 12 12" aria-hidden="true">
        <path d="M6,1 C3.8,1 2.5,2.6 2.5,4.4 C2.5,7 6,11 6,11 C6,11 9.5,7 9.5,4.4 C9.5,2.6 8.2,1 6,1 Z" fill="none" stroke="var(--paper)" stroke-width="1"/>
        <circle cx="6" cy="4.5" r="1.3" fill="var(--paper)"/>
      </svg>
      418 Harbor Crest Lane Millbrook Ohio 44210
    </p>
  </section>

</body>
</html>
```